Modern Business Card For A Digital Advertising Company

I'll be print on the Tarn Prints Velour paper http://us.tarnprints.example/products/velour/business-cards.html
Need's to be modern and use the color palette of the logo or gray scales. I think integrating the pixelation of the logo in to the card and having it wrap from one side to the other could be interesting. My company provides ad operations, web development, and number of other services to websites around the world. You can see my website at http://www.pixelharbor.example
Contact info on the card needs to have
Dana Welloby
President
p.555.318.4406
dana@pixelharbor.example
http://www.pixelharbor.example
Doesn't necessarily need to be in that order
Target Market(s)
Website owners
Industry/Entity Type
Business
Look and feel

```html
<!DOCTYPE html>
<html lang="en">
<head>
<meta charset="utf-8">
<title>Pixel Harbor – Business Card</title>
<link rel="stylesheet" href="https://fonts.googleapis.com/css2?family=Arimo:wght@400;700&family=Questrial&display=swap">
<style>
  :root {
    --backdrop: #2b2b2b;
    --green-deep: #5b8a2f;
    --green-mid: #6f9e38;
    --green-bright: #8dc63f;
    --white: #ffffff;
    --ink-dark: #3a3a3a;
  }
  html, body {
    margin: 0;
    padding: 0;
    overflow: hidden;
  }
  .stage {
    position: relative;
    width: 1200px;
    height: 450px;
    background: var(--backdrop);
    overflow: hidden;
  }
  .card {
    position: absolute;
    top: 75px;
    width: 524px;
    height: 300px;
    overflow: hidden;
    box-shadow: 0 4px 12px rgba(0,0,0,.45);
  }
  .card-front { left: 56px; background: var(--white); }
  .card-back {
    left: 620px;
    width: 523px;
    background: radial-gradient(ellipse at 50% 45%, var(--green-bright) 0%, var(--green-mid) 45%, var(--green-deep) 100%);
  }
  .swoosh { position: absolute; inset: 0; }

  .brand-front {
    position: absolute;
    left: 40px;
    top: 120px;
    font-family: "Questrial", sans-serif;
    color: var(--green-bright);
    font-size: 34px;
    line-height: 38px;
    letter-spacing: 3px;
  }
  .brand-front .brand-dot {
    display: block;
    width: 22px;
    height: 22px;
    margin-bottom: 12px;
    background: var(--green-bright);
  }

  .identity {
    position: absolute;
    right: 22px;
    top: 66px;
    text-align: right;
    font-family: "Arimo", sans-serif;
    color: var(--white);
  }
  .identity .name { font-size: 19px; font-weight: 700; line-height: 22px; }
  .identity .role { font-size: 14px; line-height: 16px; }

  .contacts {
    position: absolute;
    right: 22px;
    top: 168px;
    margin: 0;
    padding: 0;
    list-style: none;
    font-family: "Arimo", sans-serif;
    font-size: 14px;
    color: var(--white);
    text-align: right;
  }
  .contacts li { line-height: 23.5px; }
  .contacts svg { width: 11px; height: 11px; vertical-align: -1px; margin-right: 4px; }

  .brand-back {
    position: absolute;
    left: 0;
    right: 0;
    top: 70px;
    text-align: center;
    font-family: "Questrial", sans-serif;
    color: var(--white);
    font-size: 56px;
    line-height: 64px;
    letter-spacing: 4px;
  }
  .site-back {
    position: absolute;
    left: 0;
    right: 0;
    top: 234px;
    text-align: center;
    font-family: "Questrial", sans-serif;
    color: var(--white);
    font-size: 20px;
    letter-spacing: 1.5px;
  }
</style>
</head>
<body>
<main class="stage">
  <section class="card card-front">
    <svg class="swoosh" viewBox="0 0 524 300" width="524" height="300" aria-hidden="true">
      <defs>
        <linearGradient id="frontGreen" x1="0" y1="0" x2="1" y2="0">
          <stop offset="0" stop-color="#8dc63f"/>
          <stop offset="1" stop-color="#5b8a2f"/>
        </linearGradient>
      </defs>
      <path d="M234 0 C 345 55 330 215 0 300 L524 300 L524 0 Z" fill="url(#frontGreen)"/>
      <path d="M300 0 C 330 10 345 25 350 40 C 335 25 315 15 285 10 Z" fill="#8dc63f"/>
      <path d="M330 162 C 290 245 180 290 40 300 L70 300 C 200 285 300 235 330 162 Z" fill="#ffffff"/>
    </svg>

    <div class="brand-front">
      <span class="brand-dot"></span>
      PIXEL<br>HARBOR
    </div>

    <div class="identity">
      <div class="name">Dana Welloby</div>
      <div class="role">President</div>
    </div>

    <ul class="contacts">
      <li>
        <svg viewBox="0 0 12 12"><path d="M3 1 L5 3.5 L4 5 Q5 7 7 8 L8.5 7 L11 9 L9.5 11 Q4 10.5 1 3 Z" fill="#fff"/></svg>555.318.4406
      </li>
      <li>
        <svg viewBox="0 0 12 12"><rect x="1" y="3" width="10" height="7" fill="#fff"/><path d="M1 3 L6 7 L11 3" stroke="#6f9e38" fill="none"/></svg>dana@pixelharbor.example
      </li>
      <li>
        <svg viewBox="0 0 12 12"><circle cx="6" cy="6" r="5" fill="#fff"/><path d="M1 6 H11" stroke="#6f9e38"/></svg>www.pixelharbor.example
      </li>
    </ul>
  </section>

  <section class="card card-back">
    <div class="brand-back">PIXEL<br>HARBOR</div>
    <div class="site-back">www.pixelharbor.example</div>
  </section>
</main>
</body>
</html>
```